Web Design For Staffing Company

We need a homepage web design for a technical staffing company.

Please see attached brief for project details.

please make the site modern with bold colors while matching the logo

Be sure to read the attached breif in full beforehand.

Target Market(s)

technical companies looking to hire talent

Industry/Entity Type

Staffing

Number of Pages Required

1 page

Font styles to use
Sans Serif

```html
<!DOCTYPE html>
<html lang="en">
<head>
<meta charset="utf-8">
<title>Voltara Staffing – Technical Staffing</title>
<link href="https://fonts.googleapis.com/css2?family=Oswald:wght@400;500;600&family=Roboto:ital,wght@0,300;0,400;0,500;1,400&display=swap" rel="stylesheet">
<style>
:root{
  --navy:#0f2a44;
  --navy-deep:#0b1c2e;
  --blue:#2f82c5;
  --blue-bright:#3a8fd6;
  --grey-bg:#efefef;
  --text:#3c3c3c;
  --text-soft:#5a5a5a;
  --white:#ffffff;
}
*{box-sizing:border-box;margin:0;padding:0}
html,body{width:1200px;height:3334px;overflow:hidden;background:var(--white)}
body{font-family:'Roboto',sans-serif;color:var(--text);position:relative}
.heading{font-family:'Oswald',sans-serif;text-transform:uppercase}
.btn{display:inline-flex;align-items:center;justify-content:center;font-family:'Oswald',sans-serif;text-transform:uppercase;color:var(--white);border-radius:40px;text-decoration:none;font-weight:500}
.btn-blue{background:var(--blue)}
.btn-navy{background:var(--navy)}

/* header */
.site-header{position:absolute;top:0;left:0;width:1200px;height:80px;background:var(--white)}
.brand{position:absolute;left:172px;top:18px;display:flex;align-items:center;gap:10px}
.brand-mark{width:30px;height:30px;border-radius:50%;background:var(--blue)}
.brand-name{font-family:'Oswald',sans-serif;font-weight:600;font-size:30px;color:var(--navy);line-height:1}
.main-nav{position:absolute;top:28px;left:573px;display:flex;gap:0}
.main-nav a{font-family:'Oswald',sans-serif;font-weight:500;font-size:19px;color:var(--navy);text-decoration:none;text-transform:uppercase;position:absolute;white-space:nowrap}
.main-nav a.active{color:var(--blue)}
.search-bar{position:absolute;top:80px;left:0;width:1200px;height:71px;background:var(--navy)}
.search-input{position:absolute;left:243px;top:12px;width:571px;height:47px;background:var(--white);border-radius:30px;font-size:13px;font-style:italic;color:#666;padding:15px 18px}
.search-btn{position:absolute;left:821px;top:12px;width:136px;height:47px;font-size:15px}

/* hero */
.hero{position:absolute;top:151px;left:0;width:1200px;height:652px;overflow:hidden}
.hero-photo{position:absolute;inset:0;background:linear-gradient(100deg,#c9cfd4 0%,#aab3bb 30%,#7c858f 55%,#464c55 80%,#2e3239 100%)}
.hero-shade{position:absolute;inset:0;background:rgba(10,20,35,.25)}
.hero-title{position:absolute;top:190px;left:0;width:1200px;text-align:center;color:var(--white);font-size:41px;line-height:47px;font-weight:500;letter-spacing:.3px}
.hero-actions{position:absolute;top:318px;left:395px;display:flex;gap:9px}
.hero-actions .btn{width:202px;height:55px;font-size:25px}
.slider-dots{position:absolute;top:560px;left:513px;display:flex;gap:5px}
.slider-dots span{width:41px;height:3px;background:var(--white)}
.slider-dots span.dim{background:rgba(255,255,255,.45)}
.hero-wave{position:absolute;left:0;bottom:0;width:1200px;height:110px}

/* intro */
.intro{position:absolute;top:803px;left:0;width:1200px;height:326px;background:var(--grey-bg)}
.intro p{position:absolute;top:68px;left:200px;width:800px;text-align:center;font-size:24px;line-height:41px;color:#333}
.intro strong{color:var(--blue);font-weight:500}

/* features */
.feature{position:absolute;left:0;width:1200px}
.feature-art{position:absolute;border-radius:6px;background:linear-gradient(135deg,#eef3f8,#cfe0ef 60%,#e9eef3)}
.feature-copy{position:absolute;font-size:17px;line-height:28.5px;font-weight:300;color:var(--text-soft)}
.feature-actions{position:absolute;display:flex;gap:5px}
.feature-actions .btn{width:116px;height:37px;font-size:13px}
.feature-one{top:1129px;height:420px}
.feature-two{top:1549px;height:421px}

/* testimonial */
.testimonial{position:absolute;top:1970px;left:0;width:1200px;height:289px;background:linear-gradient(120deg,#2b2b2b 0%,#3d3d3d 40%,#222 75%,#333 100%);color:var(--white);text-align:center}
.testimonial h3{position:absolute;top:92px;width:100%;font-size:21px;font-weight:400}
.testimonial blockquote{position:absolute;top:136px;left:280px;width:640px;font-size:13px;font-style:italic;line-height:26px}

/* blog */
.blog-title{position:absolute;top:2296px;left:0;width:1200px;text-align:center;font-size:47px;font-weight:500;color:#111}
.post{position:absolute;top:2379px;width:268px;height:368px;background:#ebebeb}
.post-photo{height:180px}
.post-date{position:absolute;top:215px;left:31px;background:var(--blue);color:var(--white);font-size:12px;font-weight:500;padding:5px 8px;display:flex;align-items:center;gap:4px}
.post-title{position:absolute;top:258px;left:31px;width:225px;font-size:16px;line-height:24.5px;font-weight:500;color:#555}
.post-arrow{position:absolute;top:341px;left:31px}

/* calls to action */
.cta{position:absolute;top:2826px;height:217px;width:600px;text-align:center;color:var(--white)}
.cta-left{left:0;background:linear-gradient(135deg,#2e7dc0,#2a6fae)}
.cta-right{left:600px;background:linear-gradient(135deg,#1f6aae,#19609f)}
.cta h4{margin-top:60px;font-size:21px;line-height:26px;font-weight:500}
.cta .btn-outline{margin-top:22px;width:200px;height:40px;border:2px solid var(--white);font-size:14px;background:transparent}

/* footer */
.site-footer{position:absolute;top:3043px;left:0;width:1200px;height:291px;background:var(--navy-deep);color:var(--white)}
.footer-brand{position:absolute;left:172px;top:56px;display:flex;align-items:center;gap:10px}
.footer-col{position:absolute;top:53px;width:160px}
.footer-col h5{font-size:19px;font-weight:500;margin-bottom:10px}
.footer-col p{font-size:12px;line-height:15px}
.footer-col .btn{position:absolute;top:113px;left:0;width:147px;height:36px;font-size:13px;gap:6px}
.footer-rule{position:absolute;top:228px;left:188px;width:840px;height:1px;background:rgba(255,255,255,.2)}
.copyright{position:absolute;top:258px;width:100%;text-align:center;font-size:11px}
.footer-code{position:absolute;top:234px;left:1130px;font-size:11px}
</style>
</head>
<body>

<header class="site-header">
  <div class="brand"><span class="brand-mark"></span><span class="brand-name">Voltara</span></div>
  <nav class="main-nav">
    <a class="active" href="#" style="left:0">Home</a>
    <a href="#" style="left:77px">About</a>
    <a href="#" style="left:162px">Job Seekers</a>
    <a href="#" style="left:296px">Clients</a>
    <a href="#" style="left:391px">Contact</a>
  </nav>
</header>
<div class="search-bar">
  <div class="search-input">Keyword &amp; Location</div>
  <a class="btn btn-blue search-btn" href="#">Search Jobs</a>
</div>

<section class="hero">
  <div class="hero-photo" role="img" aria-label="Photo of job candidates in business attire waiting with laptops and tablets"></div>
  <div class="hero-shade"></div>
  <h1 class="heading hero-title">The Right People for the Right Jobs!<br>Bridging the Talent Gap in Technical Staffing</h1>
  <div class="hero-actions">
    <a class="btn btn-navy" href="#">Hire Talent</a>
    <a class="btn btn-blue" href="#">Get Hired</a>
  </div>
  <div class="slider-dots"><span></span><span></span><span class="dim"></span><span></span></div>
  <svg class="hero-wave" viewBox="0 0 1200 110" preserveAspectRatio="none">
    <path d="M0,58 C250,100 420,115 600,110 C860,110 1080,80 1200,0 L1200,110 L0,110 Z" fill="#efefef"/>
  </svg>
</section>

<section class="intro">
  <p><strong>Voltara Staffing</strong> is a National Technical Staffing and Recruiting Solutions Provider founded in 2013 focused on matching contract and full time Engineering and IT professionals with new and exciting employment opportunities!</p>
</section>

<section class="feature feature-one">
  <div class="feature-art" role="img" aria-label="Illustration of a recruiter examining candidate profiles with a magnifying glass" style="left:100px;top:49px;width:375px;height:313px"></div>
  <p class="feature-copy" style="left:531px;top:102px;width:500px">Simply said… WE LOVE TO RECRUIT! It's our passion and we take it very seriously! It is not easy for JOB SEEKERS to put their job search efforts and trust in the hands of someone else, especially when there are so many Staffing Firms to choose from. So how do you know you are choosing the best Staffing Representation possible?</p>
  <div class="feature-actions" style="left:528px;top:290px">
    <a class="btn btn-blue" href="#">Learn More</a>
    <a class="btn btn-navy" href="#">View Jobs</a>
  </div>
</section>

<section class="feature feature-two">
  <div class="feature-art" role="img" aria-label="Illustration of a businessman beside a large candidate résumé with icons" style="left:713px;top:17px;width:357px;height:350px"></div>
  <p class="feature-copy" style="left:172px;top:83px;width:505px">Are you responsible for Technical Staffing within your organization? Are you satisfied with your current Supplier(s)' overall performance? Does it appear they identify potential Candidate(s) based purely on "buzz-word" searches? Is it evident they just do not grasp the scope and responsibilities of your technical staffing need(s)?</p>
  <div class="feature-actions" style="left:169px;top:276px">
    <a class="btn btn-blue" href="#">Learn More</a>
    <a class="btn btn-navy" href="#">Hire Talent</a>
  </div>
</section>

<section class="testimonial">
  <h3>Sam R. – Electrical Test Engineer in the Automotive Sector.</h3>
  <blockquote>"Dean Marsh is an excellent recruiter. He is articulate, honest, has a good nature and is an effective information conduit between his clients and candidates. He gave me the feeling he isthere for the big picture desiring to forge a future relationship that will be mutually beneficial to both of us."</blockquote>
</section>

<h2 class="heading blog-title">Latest Blog</h2>

<article class="post" style="left:172px">
  <div class="post-photo" role="img" aria-label="Photo of a woman working on a laptop at a table" style="background:linear-gradient(135deg,#cfc4b8,#8a7a6a 55%,#3d3a3a)"></div>
  <span class="post-date"><svg width="11" height="11" viewBox="0 0 11 11"><rect x="1" y="2" width="9" height="8" fill="none" stroke="#fff"/><line x1="1" y1="4.5" x2="10" y2="4.5" stroke="#fff"/></svg>JUNE 25 2020</span>
  <h6 class="post-title">Ways To Make The Most Of The Hot Job Market</h6>
  <svg class="post-arrow" width="26" height="8" viewBox="0 0 26 8"><line x1="0" y1="4" x2="24" y2="4" stroke="#222" stroke-width="1.3"/><path d="M20,1 L24,4 L20,7" fill="none" stroke="#222" stroke-width="1.3"/></svg>
</article>
<article class="post" style="left:465px">
  <div class="post-photo" role="img" aria-label="Photo of two business people shaking hands" style="background:linear-gradient(135deg,#6f8fb0,#c9d3dc 50%,#34496a)"></div>
  <span class="post-date"><svg width="11" height="11" viewBox="0 0 11 11"><rect x="1" y="2" width="9" height="8" fill="none" stroke="#fff"/><line x1="1" y1="4.5" x2="10" y2="4.5" stroke="#fff"/></svg>JUNE 25 2020</span>
  <h6 class="post-title">Back To Basics: Meeting Employees' Needs To Improve Organizational Performance</h6>
  <svg class="post-arrow" width="26" height="8" viewBox="0 0 26 8"><line x1="0" y1="4" x2="24" y2="4" stroke="#222" stroke-width="1.3"/><path d="M20,1 L24,4 L20,7" fill="none" stroke="#222" stroke-width="1.3"/></svg>
</article>
<article class="post" style="left:759px">
  <div class="post-photo" role="img" aria-label="Black and white portrait photo with a quotation about technology" style="background:linear-gradient(135deg,#5a5a5a,#2a2a2a 60%,#111)"></div>
  <span class="post-date"><svg width="11" height="11" viewBox="0 0 11 11"><rect x="1" y="2" width="9" height="8" fill="none" stroke="#fff"/><line x1="1" y1="4.5" x2="10" y2="4.5" stroke="#fff"/></svg>JUNE 25 2020</span>
  <h6 class="post-title">5 Important Takeaways From Lumora's Two-Year Study Of Remote Work</h6>
  <svg class="post-arrow" width="26" height="8" viewBox="0 0 26 8"><line x1="0" y1="4" x2="24" y2="4" stroke="#222" stroke-width="1.3"/><path d="M20,1 L24,4 L20,7" fill="none" stroke="#222" stroke-width="1.3"/></svg>
</article>

<section class="cta cta-left" role="img" aria-label="Blue-tinted photo of a crowd of professionals">
  <h4 class="heading">Looking for a career-minded<br>candidates?</h4>
  <a class="btn btn-outline" href="#">Request Talent</a>
</section>
<section class="cta cta-right" role="img" aria-label="Blue-tinted photo of a crowd of professionals">
  <h4 class="heading">Looking for career<br>opportunities?</h4>
  <a class="btn btn-outline" href="#">Search Jobs</a>
</section>

<footer class="site-footer">
  <div class="footer-brand"><span class="brand-mark"></span><span class="brand-name" style="color:#fff">Voltara</span></div>
  <div class="footer-col" style="left:417px">
    <h5 class="heading">Get Hired</h5>
    <p>Sed ut perspiciatis unde omnis iste natusor sit volu ptatem accusantium</p>
    <a class="btn btn-blue" href="#"><svg width="12" height="12" viewBox="0 0 12 12"><circle cx="5" cy="5" r="3.8" fill="none" stroke="#fff" stroke-width="1.5"/><line x1="8" y1="8" x2="11" y2="11" stroke="#fff" stroke-width="1.6"/></svg>Search Now</a>
  </div>
  <div class="footer-col" style="left:634px">
    <h5 class="heading">Hire Talent</h5>
    <p>Sed ut perspiciatis unde omnis iste natusor sit volu ptatem accusantium</p>
    <a class="btn btn-blue" href="#"><svg width="12" height="12" viewBox="0 0 12 12"><circle cx="6" cy="3.5" r="3" fill="#fff"/><path d="M0.5,12 C1,7.5 11,7.5 11.5,12 Z" fill="#fff"/></svg>Start Today</a>
  </div>
  <div class="footer-col" style="left:845px;width:185px">
    <h5 class="heading">Address</h5>
    <p>Voltara Staffing, Inc. 48 Harbor Lane, Suite 2, Riverton, MA 01990</p>
    <a class="btn btn-blue" href="#"><svg width="13" height="10" viewBox="0 0 13 10"><rect x="0.5" y="0.5" width="12" height="9" fill="#fff"/><path d="M0.5,0.5 L6.5,5.5 L12.5,0.5" fill="none" stroke="#2f82c5"/></svg>Contact Us</a>
  </div>
  <div class="footer-rule"></div>
  <span class="footer-code">C4</span>
  <p class="copyright">Copyright 2020 All Rights Reserved</p>
</footer>

</body>
</html>
```